Roofing company in Toronto, Canada needs a logo design and business card design

We need a business card and logo created for our company. Our company is "KMB Roofing" which provides roofing services for commercial and residential customers. We serve customers in the Greater Toronto Area (in Canada) thus the name KMB.

We want the logo and business card to be a modern design displaying professionalism and quality in the work. We would prefer rounded corners for the business cards but are open to other ideas. The cards should be pleasant and appealing to customers.

Target Market(s)

Commercial and Residential customers

Industry/Entity Type

Roofing

Contact Information for Business Card

Logo Text

KMB Roofing

Requirements
Nice to have
• Colours that are pleasing to the eye but at the same time should stand out from other business cards. If the design can incorporate the name of KMB Roofing and the actual concept of roofing that would be nice.
Should not have
• Do not want the business cards or logo to be childish looking. Need to look professionally designed.

```html
<!DOCTYPE html>
<html lang="en">
<head>
<meta charset="utf-8">
<title>KMB Roofing business cards</title>
<link href="https://fonts.googleapis.com/css2?family=Open+Sans:wght@400;600;700&display=swap" rel="stylesheet">
<style>
  :root {
    --backdrop: #b8b8b8;
    --card-white: #fdfdfd;
    --card-black: #050507;
    --brand-red: #b5121b;
    --ink: #333333;
    --ink-soft: #444444;
    --white: #f2f2f2;
  }
  html, body {
    margin: 0;
    padding: 0;
    width: 1200px;
    height: 900px;
    overflow: hidden;
    background: var(--backdrop);
    font-family: "Open Sans", Arial, sans-serif;
  }
  .canvas {
    position: relative;
    width: 1200px;
    height: 900px;
  }
  .card {
    position: absolute;
    top: 271px;
    width: 457px;
    height: 282px;
    border-radius: 14px;
    box-shadow: 2px 3px 5px rgba(0,0,0,0.35);
    overflow: hidden;
  }
  .card-front {
    left: 137px;
    background: var(--card-white);
  }
  .card-back {
    left: 626px;
    background:
      radial-gradient(ellipse 70px 150px at 50% 100%, rgba(120,120,125,0.5), rgba(20,20,24,0) 100%),
      linear-gradient(180deg, #0a0a0d 0%, var(--card-black) 100%);
  }
  .wordmark {
    position: absolute;
    font-weight: 700;
    letter-spacing: 0.3px;
    white-space: nowrap;
    display: flex;
    align-items: center;
    line-height: 1;
  }
  .wordmark-square {
    display: inline-block;
    background: currentColor;
    flex: none;
  }
  .card-front .wordmark {
    left: 30px;
    width: 196px;
    top: 130px;
    gap: 8px;
    font-size: 25px;
    color: var(--brand-red);
  }
  .card-front .wordmark-square { width: 12px; height: 12px; }
  .card-back .wordmark {
    left: 0;
    right: 0;
    top: 121px;
    gap: 12px;
    justify-content: center;
    font-size: 42px;
    color: var(--white);
  }
  .card-back .wordmark-square { width: 18px; height: 18px; }
  .contact-block {
    position: absolute;
    left: 246px;
    top: 62px;
    width: 200px;
    color: var(--ink);
  }
  .person-name {
    margin: 0;
    font-size: 20px;
    font-weight: 600;
    color: var(--brand-red);
    letter-spacing: 0.2px;
    line-height: 24px;
    white-space: nowrap;
  }
  .person-role {
    margin: 0 0 16px;
    font-size: 15px;
    font-weight: 600;
    color: var(--ink);
    line-height: 18px;
  }
  .contact-list {
    list-style: none;
    margin: 0 0 12px;
    padding: 0;
  }
  .contact-item {
    display: flex;
    align-items: center;
    font-size: 13.5px;
    line-height: 20.5px;
    color: var(--ink-soft);
    white-space: nowrap;
  }
  .contact-icon {
    width: 12px;
    height: 12px;
    margin-right: 10px;
    flex: none;
  }
  .postal-address {
    font-style: normal;
    font-size: 12.5px;
    line-height: 17px;
    color: var(--ink-soft);
    white-space: nowrap;
  }
</style>
</head>
<body>
<main class="canvas">
  <section class="card card-front" aria-label="Business card front">
    <div class="wordmark"><span class="wordmark-square"></span>KMB Roofing</div>
    <div class="contact-block">
      <h1 class="person-name">DANIEL MORROW</h1>
      <p class="person-role">Director</p>
      <ul class="contact-list">
        <li class="contact-item">
          <svg class="contact-icon" viewBox="0 0 12 12" aria-hidden="true">
            <rect x="3" y="0.5" width="6" height="11" rx="1.2" fill="none" stroke="#b5121b" stroke-width="1.3"/>
            <rect x="5" y="9" width="2" height="1" fill="#b5121b"/>
          </svg>+61-400 555 012
        </li>
        <li class="contact-item">
          <svg class="contact-icon" viewBox="0 0 12 12" aria-hidden="true">
            <rect x="0.5" y="2.5" width="11" height="7" fill="#b5121b"/>
            <path d="M0.8 3 L6 6.8 L11.2 3" fill="none" stroke="#fff" stroke-width="1"/>
          </svg>info@kmbroofs.com
        </li>
        <li class="contact-item">
          <svg class="contact-icon" viewBox="0 0 12 12" aria-hidden="true">
            <rect x="0.5" y="0.5" width="11" height="11" rx="2" fill="#b5121b"/>
            <circle cx="6" cy="6.5" r="2.4" fill="none" stroke="#fff" stroke-width="1.1"/>
          </svg>www.kmbroofing.com
        </li>
      </ul>
      <address class="postal-address">PO Box 482, Maple Grove<br>ONT 4821 CANADA</address>
    </div>
  </section>

  <section class="card card-back" aria-label="Business card back">
    <div class="wordmark"><span class="wordmark-square"></span>KMB Roofing</div>
  </section>
</main>
</body>
</html>
```